Quillstone Business Card

We need a business card design. We have a logo from a previous Sketchfold project and I am attaching the logo files in jpeg and photoshop.

```html
<!DOCTYPE html>
<html lang="en">
<head>
<meta charset="utf-8">
<title>Quillstone Business Card</title>
<link rel="stylesheet" href="https://fonts.googleapis.com/css2?family=Montserrat:wght@500;600;700&display=swap">
<style>
  :root {
    --backdrop: #e4e4e4;
    --card: #ffffff;
    --ink: #3a3a3a;
    --slate: #4a4a4a;
    --green: #3fa34d;
    --green-light: #6cc06a;
  }
  * { margin: 0; padding: 0; box-sizing: border-box; }
  html, body {
    width: 1200px; height: 800px; overflow: hidden;
    background: var(--backdrop);
    font-family: "Montserrat", sans-serif;
  }
  .card-set {
    position: absolute; inset: 0;
    display: flex; align-items: center; justify-content: center; gap: 40px;
  }
  .card {
    position: relative; width: 540px; height: 309px;
    background: var(--card); overflow: hidden;
    box-shadow: 0 4px 14px rgba(0,0,0,0.12);
  }
  /* Front */
  .card-front { display: flex; align-items: center; justify-content: center; }
  .brand { display: flex; align-items: center; gap: 14px; }
  .brand-square { width: 30px; height: 30px; background: var(--green-light); }
  .brand-name {
    font-size: 58px; font-weight: 700; color: var(--slate); letter-spacing: -1px;
  }
  /* Back */
  .swoosh { position: absolute; left: 0; top: 0; width: 540px; height: 309px; }
  .back-brand {
    position: absolute; right: 34px; top: 58px;
    font-size: 34px; font-weight: 700; color: var(--slate); letter-spacing: -0.5px;
  }
  .contact { position: absolute; left: 34px; top: 40px; color: var(--ink); }
  .person-name {
    font-size: 20px; font-weight: 600; letter-spacing: 0.5px;
    display: flex; align-items: center; gap: 8px;
  }
  .person-name::before {
    content: ""; width: 8px; height: 8px; background: var(--ink); transform: rotate(45deg);
  }
  .person-role { font-size: 15px; font-weight: 600; color: var(--green); margin: 2px 0 0 16px; }
  .address { font-size: 14px; font-weight: 600; line-height: 1.3; margin: 28px 0 0 16px; }
  .lines { list-style: none; font-size: 14px; font-weight: 600; line-height: 1.3; margin: 18px 0 0 16px; }
  .lines .label { color: var(--green); }
</style>
</head>
<body>
  <main class="card-set">
    <section class="card card-front">
      <div class="brand">
        <span class="brand-square"></span>
        <span class="brand-name">Quillstone</span>
      </div>
    </section>

    <section class="card card-back">
      <svg class="swoosh" viewBox="0 0 540 309" aria-hidden="true">
        <path d="M0,309 L0,258 C180,256 390,228 540,140 L540,309 Z" fill="var(--green)"/>
        <path d="M0,309 L0,280 C190,274 400,240 540,160 L540,309 Z" fill="var(--slate)"/>
      </svg>
      <div class="back-brand">Quillstone</div>
      <div class="contact">
        <h1 class="person-name">YOUR NAME</h1>
        <p class="person-role">Company Position</p>
        <p class="address">111 Your Street Address<br>206 Town, CT 00000</p>
        <ul class="lines">
          <li><span class="label">E:</span> youremail@domain.com</li>
          <li><span class="label">P:</span> 111-222-444</li>
          <li><span class="label">F:</span> 111-222-333</li>
        </ul>
      </div>
    </section>
  </main>
</body>
</html>
```